Talvo shoes is a wholesale shoe sales company , mostly working in female shoes and kiddies shoes with a small mens section . looking for a clean slick look. http://www.kemrafootwear.co.za/shop/ is a good reference

It Company

```html
<!DOCTYPE html>
<html lang="en">
<head>
<meta charset="utf-8">
<title>Talvo shoes</title>
<link href="https://fonts.googleapis.com/css2?family=Open+Sans:wght@400;600;700&display=swap" rel="stylesheet">
<style>
:root{
  --orange:#e8501f;
  --ink:#333333;
  --muted:#8a8a8a;
  --topbar:#2a2a2a;
  --line:#e2e2e2;
  --footer-bg:#efefef;
  --white:#ffffff;
}
*{box-sizing:border-box;margin:0;padding:0}
html,body{width:723px;height:1200px;overflow:hidden}
body{font-family:"Open Sans",Arial,sans-serif;color:var(--ink);background:var(--white);position:relative}
.wrap{position:absolute;left:53px;width:617px}

.topbar{position:absolute;top:0;left:0;width:723px;height:46px;background:var(--topbar);color:#d8d8d8;font-size:10px}
.topbar .account{position:absolute;left:53px;top:16px}
.topbar .cart{position:absolute;right:53px;top:15px;display:flex;align-items:center;gap:6px}

.header{top:46px;height:80px}
.logo{position:absolute;left:0;top:20px;font-size:30px;font-weight:400;color:var(--ink);letter-spacing:-0.5px}
.nav{position:absolute;right:0;top:0;display:flex;height:72px}
.nav a{display:block;text-decoration:none;color:var(--ink);text-align:center;width:68px;padding-top:24px;font-size:10px;font-weight:600;border-top:3px solid transparent;border-left:1px solid var(--line)}
.nav a small{display:block;font-size:7px;font-weight:400;color:var(--muted);margin-top:3px}
.nav a.active{background:#f2f2f2;border-top-color:var(--orange)}
.nav a.wide{width:90px}

.hero{top:126px;height:310px;background:linear-gradient(160deg,#f4f4f4 0%,#dcdcdc 55%,#c9c9c9 100%)}
.hero .shoe{position:absolute;left:130px;top:20px;width:450px;height:250px;border-radius:48% 52% 38% 42%;background:linear-gradient(135deg,#2aa2b8 0%,#1f8aa0 50%,#e9457b 100%);opacity:.85}
.hero .caption{position:absolute;left:0;top:135px;width:258px;height:90px;background:rgba(60,60,60,.78);color:var(--white);padding:14px 20px}
.hero .caption h2{font-size:20px;font-weight:600;letter-spacing:.5px}
.hero .caption p{font-size:9px;line-height:1.35;margin-top:4px;color:#e6e6e6}
.hero .arrows{position:absolute;left:14px;bottom:18px;display:flex;gap:6px}

.features{top:436px;height:58px;display:flex;border-bottom:1px solid var(--line)}
.feature{flex:1;display:flex;align-items:center;gap:10px;padding-left:10px;background:#f7f7f7}
.feature.active{background:#ececec}
.feature .num{width:30px;height:30px;border-radius:50%;background:var(--orange);color:var(--white);font-weight:700;font-size:14px;display:flex;align-items:center;justify-content:center}
.feature h3{font-size:13px;font-weight:400}
.feature.active h3{color:var(--orange)}
.feature p{font-size:7px;color:var(--muted);margin-top:2px}

.arrivals-title{top:516px;text-align:center;font-size:17px;font-weight:400}
.products{top:558px;display:flex;justify-content:space-between;padding:0 2px}
.product{width:124px;height:166px;border:1px solid var(--line);text-align:center;padding-top:14px}
.product .photo{width:90px;height:62px;margin:0 auto;border-radius:30px 40px 12px 12px}
.product h4{font-size:8px;font-weight:400;color:#555;margin-top:18px}
.product .price{font-size:9px;font-weight:700;margin-top:8px}
.product .stars{margin-top:6px;font-size:9px;color:#b5b5b5;letter-spacing:2px}

.footer-links{position:absolute;top:772px;left:0;width:723px;height:240px;background:var(--footer-bg)}
.col{position:absolute;top:24px}
.col h5{font-size:12px;font-weight:400;height:24px}
.col ul{list-style:none}
.col li{font-size:7.5px;color:#666;line-height:16.5px}

.bottom{top:1012px;height:188px}
.bottom h5{position:absolute;top:26px;font-size:10px;font-weight:600;letter-spacing:.3px}
.bottom .blurb{position:absolute;top:46px;font-size:7.5px;color:#666;line-height:1.4}
.signup{position:absolute;left:0;top:84px;display:flex}
.signup .field{width:100px;height:20px;border:1px solid #cfcfcf}
.signup .btn{height:20px;padding:0 10px;background:#2b9be0;color:var(--white);font-size:8px;font-weight:600;display:flex;align-items:center}
.cards{position:absolute;left:260px;top:48px;display:flex;flex-wrap:wrap;width:170px;gap:8px 8px}
.cards span{width:34px;height:18px;border-radius:3px;background:#d7dbe3}
.social{position:absolute;left:477px;top:82px;display:flex;gap:5px}
.social span{width:18px;height:18px}
.copyright{position:absolute;top:144px;left:0;width:617px;border-top:1px solid var(--line);padding-top:12px;font-size:7.5px;color:#777}
</style>
</head>
<body>

<div class="topbar">
  <span class="account">Register &nbsp;|&nbsp; Login &nbsp;|&nbsp; My Account</span>
  <span class="cart">
    <svg width="12" height="11" viewBox="0 0 12 11"><path d="M0 1h2l2 6h6l1.5-4.5H3" fill="none" stroke="#d8d8d8" stroke-width="1.2"/><circle cx="5" cy="9.5" r="1" fill="#d8d8d8"/><circle cx="9" cy="9.5" r="1" fill="#d8d8d8"/></svg>
    Cart (0) Items
  </span>
</div>

<header class="wrap header">
  <div class="logo">Talvo shoes</div>
  <nav class="nav">
    <a class="active" href="#">HOME<small>all about shoes</small></a>
    <a href="#">ABOUT US<small>who we are</small></a>
    <a href="#">MEN<small>shoes for men</small></a>
    <a class="wide" href="#">LADIES &amp; KIDS<small>women and children</small></a>
    <a href="#">CONTACT<small>get in touch</small></a>
  </nav>
</header>

<section class="wrap hero">
  <div class="shoe" role="img" aria-label="Photo of a turquoise and pink running shoe"></div>
  <div class="caption">
    <h2>AENEAN COMDO</h2>
    <p>Donec quam felis ultricies nec pellentesque eu, pretium quis sem nulla consequat massa quis enim.</p>
  </div>
  <div class="arrows">
    <svg width="14" height="22" viewBox="0 0 14 22"><path d="M11 2L3 11l8 9" fill="none" stroke="#ffffff" stroke-width="2"/></svg>
    <svg width="14" height="22" viewBox="0 0 14 22"><path d="M3 2l8 9-8 9" fill="none" stroke="#ffffff" stroke-width="2"/></svg>
  </div>
</section>

<section class="wrap features">
  <div class="feature"><span class="num">1</span><div><h3>Female Shoes</h3><p>Lorem ipsum dolor sit amet</p></div></div>
  <div class="feature active"><span class="num">2</span><div><h3>Men's Shoes</h3><p>Lorem ipsum dolor sit amet</p></div></div>
  <div class="feature"><span class="num">3</span><div><h3>Kiddies Shoes</h3><p>Lorem ipsum dolor sit amet</p></div></div>
</section>

<h2 class="wrap arrivals-title">New Arrivals</h2>

<section class="wrap products">
  <div class="product"><div class="photo" role="img" aria-label="Photo of a navy canvas sneaker" style="background:linear-gradient(135deg,#5c6a86,#2f3a52)"></div><h4>COMBINED JACKET</h4><div class="price">$119.50</div><div class="stars">★★★★★</div></div>
  <div class="product"><div class="photo" role="img" aria-label="Photo of a black polka dot high heel" style="background:linear-gradient(135deg,#3a3a3a,#111111)"></div><h4>COMBINED JACKET</h4><div class="price">$119.50</div><div class="stars">★★★★★</div></div>
  <div class="product"><div class="photo" role="img" aria-label="Photo of a red and grey sneaker" style="background:linear-gradient(135deg,#c94a4a,#8a8a8a)"></div><h4>COMBINED JACKET</h4><div class="price">$119.50</div><div class="stars">★★★★★</div></div>
  <div class="product"><div class="photo" role="img" aria-label="Photo of a beige and red sneaker" style="background:linear-gradient(135deg,#e8d7b8,#c0392b)"></div><h4>COMBINED JACKET</h4><div class="price">$119.50</div><div class="stars">★★★★★</div></div>
</section>

<section class="footer-links">
  <div class="col" style="left:53px"><h5>Woman</h5><ul><li>Lorem ipsum</li><li>Aenean massa</li><li>Adipiscing elit</li><li>Recreational</li><li>Interdum et amet</li><li>Natoque penatibus</li><li>Natoque penatibus</li><li>Commodo ligula</li><li>Nascetaur adipiscing</li></ul></div>
  <div class="col" style="left:188px"><h5>&nbsp;</h5><ul><li>Lorem ipsum</li><li>Aenean massa</li><li>Adipiscing elit</li><li>Recreational</li><li>Interdum et amet</li><li>Natoque penatibus</li><li>Natoque penatibus</li><li>Commodo ligula</li><li>Nascetaur adipiscing</li></ul></div>
  <div class="col" style="left:325px"><h5>&nbsp;</h5><ul><li>Lorem ipsum</li><li>Aenean massa</li><li>Adipiscing elit</li><li>Recreational</li></ul></div>
  <div class="col" style="left:434px"><h5>Men</h5><ul><li>Lorem ipsum</li><li>Aenean massa</li><li>Adipiscing elit</li><li>Recreational</li><li>Interdum et amet</li><li>Natoque penatibus</li><li>Natoque penatibus</li><li>Commodo ligula</li><li>Nascetaur adipiscing</li></ul></div>
  <div class="col" style="left:578px"><h5>Brands</h5><ul><li>Lorem ipsum</li><li>Aenean massa</li><li>Adipiscing elit</li><li>Recreational</li><li>Interdum et amet</li><li>Natoque penatibus</li><li>Natoque penatibus</li><li>Commodo ligula</li><li>Nascetaur adipiscing</li></ul></div>
</section>

<footer class="wrap bottom">
  <h5 style="left:0">NEWSLETTER SIGNUP</h5>
  <p class="blurb" style="left:0;width:200px">Stay in touch with us by signing up for our quarterly newsletter today</p>
  <div class="signup"><span class="field"></span><span class="btn">SUBSCRIBE</span></div>

  <h5 style="left:260px">WE ACCEPT</h5>
  <div class="cards"><span></span><span></span><span></span><span></span><span></span></div>

  <h5 style="left:477px">GET IN TOUCH</h5>
  <p class="blurb" style="left:477px;width:140px">Follow our news and events through social channels and get our latest updates</p>
  <div class="social"><span style="background:#3b5998"></span><span style="background:#2fa8e0"></span><span style="background:#f08a24"></span></div>

  <p class="copyright">Copyright © 2013. All Rights Reserved.</p>
</footer>

</body>
</html>
```